Business card for a doctor's practice

Would like a business card for a Pulmonary ( lung) doctor. I would like to include a logo with something in reference to air or oxygen or lungs. Would like the color red included somehow. Name of the company is Breathwell Medical Associates of Eastern Carolina and we specialize in Pulmonary Medicine,. I would like something streamlined and modern
Target Market(s)
Patients, hospitals, other doctors
Industry/Entity Type
Business
Contact Information for Business Card
Would like business details superimposed on a logo somehow
Look and feel

```html
<!DOCTYPE html>
<html lang="en">
<head>
<meta charset="UTF-8">
<title>Breathwell Medical Associates – Business Card</title>
<link href="https://fonts.googleapis.com/css2?family=Cinzel:wght@500&family=Source+Sans+3:wght@400;600&display=swap" rel="stylesheet">
<style>
  :root {
    --red: #e52b25;
    --charcoal: #444446;
    --ink: #1c1c1c;
    --paper: #ffffff;
    --backdrop: #ece7df;
    --light-text: #d9d9d9;
  }
  * { margin: 0; padding: 0; box-sizing: border-box; }
  html, body { width: 1181px; height: 1200px; overflow: hidden; }
  body {
    position: relative;
    background: var(--backdrop);
    font-family: "Source Sans 3", Arial, sans-serif;
    color: var(--ink);
  }
  .card {
    position: absolute;
    left: 230px;
    width: 722px;
    height: 455px;
    border-radius: 22px;
    overflow: hidden;
  }
  .card--front { top: 101px; background: var(--paper); }
  .card--back { top: 643px; background: var(--charcoal); }

  .name-block {
    position: absolute;
    left: 18px;
    top: 74px;
    height: 70px;
    padding-left: 22px;
    border-left: 11px solid var(--red);
  }
  .name-block__name {
    font-family: "Cinzel", Georgia, serif;
    font-weight: 500;
    font-size: 25px;
    line-height: 1;
    margin-top: 12px;
    letter-spacing: 0.3px;
  }
  .name-block__title {
    color: var(--red);
    font-size: 18px;
    margin-top: 4px;
  }

  .contact { position: absolute; left: 18px; top: 263px; list-style: none; }
  .contact__item {
    display: flex;
    align-items: flex-start;
    font-size: 16px;
    line-height: 23px;
    margin-bottom: 5px;
  }
  .contact__icon { width: 32px; flex: none; padding-top: 4px; }
  .contact__icon svg { display: block; fill: var(--red); }

  .brand { position: absolute; display: flex; align-items: center; }
  .brand__mark { flex: none; background: var(--red); border-radius: 8px; }
  .brand__name { font-weight: 600; line-height: 1.15; }

  .brand--front { left: 412px; top: 324px; }
  .brand--front .brand__mark { width: 62px; height: 62px; margin-right: 11px; }
  .brand--front .brand__name { font-size: 16px; color: var(--ink); width: 210px; }

  .brand--back { left: 132px; top: 186px; }
  .brand--back .brand__mark { width: 100px; height: 100px; border-radius: 12px; margin-right: 18px; }
  .brand--back .brand__name { font-size: 28px; color: var(--light-text); width: 340px; }

  .footer-band { position: absolute; left: 0; bottom: 0; width: 722px; height: 38px; display: block; }
</style>
</head>
<body>
  <section class="card card--front">
    <div class="name-block">
      <p class="name-block__name">Your Name</p>
      <p class="name-block__title">Job Title</p>
    </div>

    <ul class="contact">
      <li class="contact__item">
        <span class="contact__icon"><svg width="12" height="15" viewBox="0 0 12 15"><path d="M6 0a6 6 0 0 0-6 6c0 4.5 6 9 6 9s6-4.5 6-9a6 6 0 0 0-6-6zm0 8.3A2.3 2.3 0 1 1 6 3.7a2.3 2.3 0 0 1 0 4.6z"/></svg></span>
        <span>00/00, Street name<br>City, St. 00000</span>
      </li>
      <li class="contact__item">
        <span class="contact__icon"><svg width="17" height="13" viewBox="0 0 17 13"><path d="M0 4c0-2 4-4 8.5-4S17 2 17 4v1.5h-4V3.5H4v2H0zM3 7h11l2 6H1z"/></svg></span>
        <span>000 000 0000</span>
      </li>
      <li class="contact__item">
        <span class="contact__icon"><svg width="10" height="15" viewBox="0 0 10 15"><path d="M1.5 0h7A1.5 1.5 0 0 1 10 1.5v12A1.5 1.5 0 0 1 8.5 15h-7A1.5 1.5 0 0 1 0 13.5v-12A1.5 1.5 0 0 1 1.5 0zM1.6 2v9.5h6.8V2zM5 12.3a.9.9 0 1 0 0 1.8.9.9 0 0 0 0-1.8z"/></svg></span>
        <span>000 000 0000</span>
      </li>
      <li class="contact__item">
        <span class="contact__icon"><svg width="16" height="11" viewBox="0 0 16 11"><path d="M0 0h16v11H0zM1.5 1.2 8 6.3l6.5-5.1z" fill-rule="evenodd"/></svg></span>
        <span>youremail@xyz.com</span>
      </li>
    </ul>

    <div class="brand brand--front">
      <span class="brand__mark"></span>
      <p class="brand__name">Breathwell Medical Associates of Eastern Carolina</p>
    </div>

    <svg class="footer-band" viewBox="0 0 722 38" preserveAspectRatio="none">
      <polygon points="0,0 377,0 398,38 0,38" fill="var(--red)"/>
      <polygon points="387,0 722,0 722,38 410,38" fill="var(--charcoal)"/>
    </svg>
  </section>

  <section class="card card--back">
    <div class="brand brand--back">
      <span class="brand__mark"></span>
      <p class="brand__name">Breathwell Medical Associates of Eastern Carolina</p>
    </div>
  </section>
</body>
</html>
```